Business Card Design Project

I need a business card for a Management Consultancy. We work with organisational design and development and strategic change using facilitation, consulting and coaching.

Size of card is 90 x 55mm.

Logo is attached.

Wording is:

Maria Kestle
Director

tel 0491627358
email is: info@tallowpoint.com.au

Target Market(s)

Government departments and not for profit organisations mainly.

Industry/Entity Type

Business

Requirements
Must have
• White or colour background not black.

On one side of the card, either back or front please include the words:

Leading Strategic Change

Two sided business card

```html
<!DOCTYPE html>
<html lang="en">
<head>
<meta charset="utf-8">
<title>TallowPoint Business Card</title>
<link rel="stylesheet" href="https://fonts.googleapis.com/css2?family=Open+Sans:wght@400;600;700&display=swap">
<style>
  :root {
    --page-bg: #e4e6e9;
    --card-white: #ffffff;
    --slate: #5d6472;
    --slate-light: #737a88;
    --slate-dark: #4c525e;
    --leaf: #6cb33f;
    --ink: #5a606b;
    --rule: #b9bdc4;
    --mark-ring: #8fb8d0;
  }
  * { box-sizing: border-box; margin: 0; padding: 0; }
  html, body {
    width: 1200px;
    height: 900px;
    overflow: hidden;
    background: var(--page-bg);
    font-family: "Open Sans", Arial, sans-serif;
  }
  .sheet {
    width: 1200px;
    height: 900px;
    display: flex;
    align-items: center;
    justify-content: center;
    gap: 40px;
  }
  .card {
    position: relative;
    width: 540px;
    height: 330px;
    box-shadow: 0 10px 28px rgba(40, 45, 55, 0.22);
    overflow: hidden;
  }

  /* Back side */
  .card--back {
    background: radial-gradient(circle at 68% 45%, var(--slate-light) 0%, var(--slate) 55%, var(--slate-dark) 100%);
  }
  .card--back .wordmark {
    position: absolute;
    left: 44px;
    top: 126px;
    font-size: 40px;
    font-weight: 600;
    letter-spacing: -0.5px;
    color: var(--card-white);
  }
  .card--back .wordmark-rule {
    position: absolute;
    left: 44px;
    top: 184px;
    width: 236px;
    height: 1px;
    background: rgba(255, 255, 255, 0.55);
  }
  .card--back .tagline {
    position: absolute;
    left: 44px;
    top: 190px;
    width: 236px;
    font-size: 12px;
    letter-spacing: 1.6px;
    color: var(--leaf);
    white-space: nowrap;
  }

  /* Front side */
  .card--front { background: var(--card-white); }
  .brand {
    position: absolute;
    left: 32px;
    top: 26px;
    display: flex;
    align-items: center;
    gap: 16px;
  }
  .brand-dot {
    width: 62px;
    height: 62px;
    border-radius: 50%;
    background: var(--mark-ring);
  }
  .brand-name {
    font-size: 40px;
    font-weight: 600;
    letter-spacing: -0.5px;
    color: var(--slate);
  }
  .brand-rule {
    position: absolute;
    left: 110px;
    top: 90px;
    width: 400px;
    height: 1px;
    background: var(--rule);
  }
  .brand-tagline {
    position: absolute;
    left: 110px;
    top: 95px;
    width: 400px;
    text-align: right;
    font-size: 12px;
    letter-spacing: 1.6px;
    color: var(--leaf);
  }
  .person {
    position: absolute;
    left: 32px;
    top: 124px;
  }
  .person-name {
    font-size: 21px;
    font-weight: 600;
    color: var(--leaf);
  }
  .person-role {
    font-size: 13px;
    color: var(--ink);
    margin-top: 2px;
  }
  .person-rule {
    width: 200px;
    height: 1px;
    background: var(--rule);
    margin: 10px 0;
  }
  .contact-list {
    list-style: none;
    font-size: 12.5px;
    line-height: 1.6;
    color: var(--ink);
  }
  .contact-list .label {
    color: var(--leaf);
    font-weight: 600;
    display: inline-block;
    width: 14px;
  }
  .address {
    position: absolute;
    right: 32px;
    bottom: 30px;
    width: 210px;
    font-size: 12.5px;
    line-height: 1.6;
    font-weight: 600;
    font-style: normal;
    color: var(--ink);
  }
  .address-rule {
    height: 1px;
    background: var(--rule);
    margin-bottom: 10px;
  }
  .address .web-name { color: var(--leaf); }
</style>
</head>
<body>
  <main class="sheet">
    <section class="card card--back" aria-label="Card back">
      <div class="wordmark">TallowPoint</div>
      <div class="wordmark-rule"></div>
      <p class="tagline">Leading Strategic Change</p>
    </section>

    <section class="card card--front" aria-label="Card front">
      <div class="brand">
        <span class="brand-dot" aria-hidden="true"></span>
        <span class="brand-name">TallowPoint</span>
      </div>
      <div class="brand-rule"></div>
      <p class="brand-tagline">Leading Strategic Change</p>

      <div class="person">
        <h1 class="person-name">Maria Kestle</h1>
        <p class="person-role">Director</p>
        <div class="person-rule"></div>
        <ul class="contact-list">
          <li><span class="label">t</span>0491627358</li>
          <li><span class="label">f</span>0491627359</li>
          <li><span class="label">e</span>info@tallowpoint.com.au</li>
        </ul>
      </div>

      <address class="address">
        <div class="address-rule"></div>
        48 Harbour Lane<br>
        Kingsford, NSW 2032<br>
        www.<span class="web-name">tallowpoint</span>.com.au
      </address>
    </section>
  </main>
</body>
</html>
```